Billboard design for a legal translations company

Dear designer, I have to renew a billboard design I used to have in my local town. We are a company that provides sworn (officially certified) translations, mainly in legal field. The billboard is located in front of the Courts building and has to be easily visible and to convey who we are a quickly. I have attached a current one, the message is the same, I will be very glad to receive your proposals and meet designers for future projects of my other companies. Thank you. SPANISH: It's about creating a billboard size (3 by 8 meters), from a sworn translation company. Attach what we had so far, the data is the same (text), but I want to change the design radically and that is even more visible. Thank you.

Target Market(s)

forreigners who are legalizing their residence or are doing any other paperwork, and companies in need of official translations.

Font styles to use
Serif

Colors

Designer to choose colors to be used in the design.

Requirements
Must have
• It is very important to convey the idea in very short glance, because it is a specific service. It has to convey seriousness too. ENGLISH: it has to be very easy to read and capture the advertising message, it has to be very visible.
Nice to have
• I would please need some element (like a stamp in the previous billboard) that would indicate what we do and call for attention. SPANISH some image of an element that makes you understand that these are official documents, right now it is the seal. It can remain a seal, or something similar.

```html
<!DOCTYPE html>
<html lang="es">
<head>
<meta charset="UTF-8">
<title>VerbaLegal – Traducciones Juradas</title>
<link rel="stylesheet" href="https://fonts.googleapis.com/css2?family=Montserrat:wght@500;600;700;800&family=Libre+Baskerville:wght@700&display=swap">
<style>
  :root{
    --stage:#e9e9e9;
    --navy:#1b2431;
    --navy-deep:#141b26;
    --white:#ffffff;
    --ink:#2b3543;
    --accent-blue:#1aa6dc;
    --accent-gold:#f0b41c;
    --seal-red:#b3141d;
    --seal-text:#fbe9c8;
    --divider:#e3b86b;
    --lang-blue:#2196d3;
    --lang-magenta:#d5408f;
    --lang-green:#8cc63f;
    --lang-teal:#21b3a0;
    --lang-orange:#f07a22;
    --lang-yellow:#f2b81c;
    --lang-lime:#9ccc3c;
  }
  *{box-sizing:border-box;margin:0;padding:0}
  html,body{width:1200px;height:565px;overflow:hidden;background:var(--stage)}
  body{font-family:"Montserrat",Arial,sans-serif;color:var(--ink)}

  .billboard{position:absolute;left:0;top:57px;width:1200px;height:450px;overflow:hidden;background:var(--white)}

  .hero{position:absolute;left:0;top:0;width:1200px;height:338px;
    background:linear-gradient(100deg,var(--navy-deep) 40%,var(--navy) 70%,#253040 100%)}
  .hero-photo{position:absolute;left:0;top:0;width:600px;height:338px}

  .seal{position:absolute;left:478px;top:154px;width:110px;height:110px;border-radius:50%;
    background:radial-gradient(circle at 45% 40%,#d3262f,var(--seal-red) 65%,#7e0d14);
    display:flex;flex-direction:column;align-items:center;justify-content:center;
    transform:rotate(-18deg);font-family:"Libre Baskerville",Georgia,serif;color:var(--seal-text);
    box-shadow:0 3px 8px rgba(0,0,0,.45)}
  .seal-percent{font-size:15px;line-height:1.1}
  .seal-word{font-size:15px;letter-spacing:.5px;line-height:1.2}

  .offer{position:absolute;left:632px;top:40px}
  .offer-item{display:flex;align-items:flex-start;color:var(--white);font-weight:700;
    font-size:40px;line-height:43px;letter-spacing:1px;text-transform:uppercase}
  .offer-item + .offer-item{margin-top:28px}
  .tick{width:22px;height:22px;margin:11px 18px 0 0;flex:none}
  .highlight{color:var(--accent-blue)}

  .languages{position:absolute;left:632px;top:241px;font-weight:500;font-size:16px;
    line-height:22px;text-transform:uppercase;letter-spacing:.2px}
  .languages span{margin-right:5px}
  .c-blue{color:var(--lang-blue)} .c-magenta{color:var(--lang-magenta)}
  .c-green{color:var(--lang-green)} .c-teal{color:var(--lang-teal)}
  .c-orange{color:var(--lang-orange)} .c-yellow{color:var(--lang-yellow)}
  .c-lime{color:var(--lang-lime)}
  .languages .more{color:var(--lang-yellow);font-size:14px}

  .brand-disc{position:absolute;left:36px;top:282px;width:232px;height:232px;border-radius:50%;
    background:var(--white);border:4px solid var(--accent-gold);border-right-color:transparent;border-bottom-color:transparent;transform:rotate(-20deg)}
  .brand{position:absolute;left:68px;top:366px;display:flex;align-items:center}
  .brand-dot{width:20px;height:20px;border-radius:50%;background:var(--accent-blue);margin-right:12px}
  .brand-name{font-weight:600;font-size:30px;color:var(--ink);letter-spacing:.2px}
  .brand-tag{position:absolute;left:100px;top:402px;font-weight:500;font-size:15px;color:var(--ink);letter-spacing:1px}

  .contact{position:absolute;top:338px;height:112px;display:flex;align-items:center}
  .phone{left:477px;font-weight:700;font-size:27px;letter-spacing:.3px}
  .web{left:651px;padding-left:28px;border-left:2px solid var(--divider);height:42px;
    flex-direction:column;align-items:flex-start;justify-content:center;top:373px;
    font-weight:700;font-size:14.5px;line-height:20px}
  .address{left:928px;padding-left:24px;border-left:2px solid var(--divider);height:42px;
    flex-direction:column;align-items:flex-start;justify-content:center;top:373px;
    font-weight:700;font-size:15.5px;line-height:21px}
</style>
</head>
<body>
<main class="billboard">
  <section class="hero">
    <svg class="hero-photo" viewBox="0 0 600 338" role="img" aria-label="Fotografía: manos revisando un documento legal con un bolígrafo y un mazo de juez sobre la mesa">
      <defs>
        <linearGradient id="photoTone" x1="0" y1="0" x2="1" y2="1">
          <stop offset="0" stop-color="#2a2420"/>
          <stop offset=".45" stop-color="#8a6a4c"/>
          <stop offset=".75" stop-color="#c9b9a2"/>
          <stop offset="1" stop-color="#5a4330"/>
        </linearGradient>
      </defs>
      <path d="M0,0 H500 C545,80 568,200 528,338 H0 Z" fill="var(--accent-gold)"/>
      <path d="M0,0 H490 C535,80 556,200 516,338 H0 Z" fill="var(--accent-blue)"/>
      <path d="M0,0 H480 C524,80 544,200 504,338 H0 Z" fill="url(#photoTone)"/>
    </svg>

    <div class="seal"><span class="seal-percent">100%</span><span class="seal-word">VALIDAS</span></div>

    <div class="offer">
      <div class="offer-item">
        <svg class="tick" viewBox="0 0 22 22" aria-hidden="true"><rect x="1.5" y="3.5" width="17" height="17" rx="2" fill="none" stroke="var(--accent-blue)" stroke-width="2.5"/><path d="M5 11 l4 4 l10 -12" fill="none" stroke="var(--accent-gold)" stroke-width="3" stroke-linecap="round" stroke-linejoin="round"/></svg>
        <div>Traducciones<br>Juradas <span class="highlight">Oficiales</span></div>
      </div>
      <div class="offer-item">
        <svg class="tick" viewBox="0 0 22 22" aria-hidden="true"><rect x="1.5" y="3.5" width="17" height="17" rx="2" fill="none" stroke="var(--accent-blue)" stroke-width="2.5"/><path d="M5 11 l4 4 l10 -12" fill="none" stroke="var(--accent-gold)" stroke-width="3" stroke-linecap="round" stroke-linejoin="round"/></svg>
        <div>Apostillas</div>
      </div>
    </div>

    <p class="languages">
      <span class="c-blue">Inglés</span><span class="c-magenta">Francés</span><span class="c-green">Portugués</span><span class="c-teal">Italiano</span><span class="c-orange">Alemán</span><span class="c-blue">Ruso</span><br>
      <span class="c-teal">Holandés</span><span class="c-orange">Rumano</span><span class="c-yellow">Árabe</span><span class="c-magenta">Polaco</span><span class="c-blue">Búlgaro</span><span class="c-lime">Húngaro</span><br>
      <span class="more">! Y más idiomas !</span>
    </p>
  </section>

  <div class="brand-disc" aria-hidden="true"></div>
  <div class="brand"><span class="brand-dot"></span><span class="brand-name">VerbaLegal</span></div>
  <div class="brand-tag">traducciones juradas</div>

  <div class="contact phone">950 213 874</div>
  <div class="contact web"><span>www.verbalegal.es</span><span>traducciones@verbalegal.es</span></div>
  <div class="contact address"><span>Calle Mayor 12</span><span>Bajo A, El Puerto</span></div>
</main>
</body>
</html>
```